Modern Business Card for Larkwell 2018

Our company assumes the best about people. We are creating an online community of entrepreneurs and business leaders who struggle with marketing their business online.

This business card should POP! We recently got a new logo and are launching a new website next month, so our business cards should make a statement that feels:
-Fresh
-Smart
-Trustworthy
-Fun

Target Market(s)

small business owners, entrepreneurs

Industry/Entity Type

Digital Marketing

Contact Information for Business Card

Dimensions: 3.5" x 2"

Font styles to use
Sans Serif

Colors
f37122
ffffff

Requirements
Must have
• We need a business card with a modern, bold design. We will use one side of the card as a lead-generation offer, so text on one side will need to fit up to 140 characters. The business card should stick to our core colors (orange, black, and white).
Nice to have
• We think a vertical "portrait" design could be interesting.
Should not have
• Should not look like a traditional business card. The round icon should stand out from a distance.

```html
<!DOCTYPE html>
<html lang="en">
<head>
<meta charset="utf-8">
<title>Larkwell Business Card</title>
<link rel="stylesheet" href="https://fonts.googleapis.com/css2?family=Lato:wght@400;900&family=Kalam:wght@700&display=swap">
<style>
  :root {
    --brand-orange: #f37122;
    --card-black: #1a1718;
    --card-white: #ffffff;
    --rule-grey: #9a9a9a;
    --page-bg: #ecebea;
  }
  * { margin: 0; padding: 0; box-sizing: border-box; }
  html, body {
    width: 1200px;
    height: 900px;
    overflow: hidden;
    background: var(--page-bg);
  }
  .canvas {
    position: relative;
    width: 1200px;
    height: 900px;
  }
  .business-card {
    position: absolute;
    left: 275px;
    top: 250px;
    width: 650px;
    height: 400px;
    filter: drop-shadow(0 10px 24px rgba(0,0,0,0.18));
  }
  .card-shape {
    position: absolute;
    inset: 0;
  }
  .brand-lockup {
    position: absolute;
    left: 0;
    top: 0;
    width: 400px;
    height: 400px;
  }
  .brand-mark {
    position: absolute;
    left: 182px;
    top: 134px;
    width: 36px;
    height: 36px;
    border-radius: 50%;
    background: var(--brand-orange);
  }
  .brand-name {
    position: absolute;
    left: 0;
    top: 186px;
    width: 400px;
    text-align: center;
    font-family: "Lato", sans-serif;
    font-weight: 900;
    font-size: 43px;
    letter-spacing: 1px;
    color: var(--brand-orange);
    line-height: 1;
  }
  .person {
    position: absolute;
    right: 36px;
    top: 36px;
    text-align: right;
  }
  .person-name {
    font-family: "Kalam", cursive;
    font-weight: 700;
    font-size: 27px;
    letter-spacing: 2px;
    color: var(--brand-orange);
    text-transform: uppercase;
    line-height: 1.1;
  }
  .person-title {
    font-family: "Lato", sans-serif;
    font-size: 19px;
    color: var(--card-white);
    margin-top: 4px;
  }
  .contact-list {
    position: absolute;
    right: 36px;
    top: 302px;
    list-style: none;
    text-align: right;
  }
  .contact-item {
    display: flex;
    justify-content: flex-end;
    align-items: center;
    gap: 8px;
    font-family: "Lato", sans-serif;
    font-size: 17px;
    color: var(--card-white);
    line-height: 23px;
  }
  .contact-icon { width: 13px; height: 13px; flex: none; }
</style>
</head>
<body>
<main class="canvas">
  <section class="business-card" aria-label="Larkwell business card">
    <svg class="card-shape" width="650" height="400" viewBox="0 0 650 400" aria-hidden="true">
      <rect x="190" y="0" width="460" height="400" fill="var(--card-black)"/>
      <rect x="300" y="135" width="350" height="133" fill="var(--card-white)"/>
      <circle cx="200" cy="200" r="196" fill="var(--card-white)" stroke="var(--brand-orange)" stroke-width="8"/>
      <line x1="388" y1="181" x2="600" y2="181" stroke="var(--rule-grey)" stroke-width="1"/>
      <line x1="388" y1="222" x2="600" y2="222" stroke="var(--rule-grey)" stroke-width="1"/>
    </svg>

    <div class="brand-lockup">
      <span class="brand-mark" aria-hidden="true"></span>
      <div class="brand-name">LARKWELL</div>
    </div>

    <div class="person">
      <div class="person-name">Dana Whitfield</div>
      <div class="person-title">Story Marketing Coach</div>
    </div>

    <ul class="contact-list">
      <li class="contact-item">
        <span>dana@larkwellnow.com</span>
        <svg class="contact-icon" viewBox="0 0 13 13" aria-hidden="true">
          <rect x="0" y="2" width="13" height="9" rx="1" fill="var(--brand-orange)"/>
          <polyline points="0.5,2.5 6.5,7 12.5,2.5" fill="none" stroke="var(--card-black)" stroke-width="1.2"/>
        </svg>
      </li>
      <li class="contact-item">
        <span>www.larkwellnow.com</span>
        <svg class="contact-icon" viewBox="0 0 13 13" aria-hidden="true">
          <circle cx="6.5" cy="6.5" r="6" fill="var(--brand-orange)"/>
          <ellipse cx="6.5" cy="6.5" rx="2.6" ry="6" fill="none" stroke="var(--card-black)" stroke-width="0.9"/>
          <line x1="0.5" y1="6.5" x2="12.5" y2="6.5" stroke="var(--card-black)" stroke-width="0.9"/>
        </svg>
      </li>
    </ul>
  </section>
</main>
</body>
</html>
```